Business incubator; Angel investments; Consulting for startups

We need new office equipment

Target Market(s)

Start up Company

Font styles to use
Sans Serif

Colors

Designer to choose only greyscale colors for use in the design.

Requirements
Must have
• Existing company logo
Nice to have
• Corporate according to the website www.tmv-norlix.com
Should not have
• Colors off gray

```html
<!DOCTYPE html>
<html lang="en">
<head>
<meta charset="utf-8">
<title>TMV Norlix Letterhead</title>
<link href="https://fonts.googleapis.com/css2?family=Montserrat:wght@400;500;600;700&display=swap" rel="stylesheet">
<style>
:root{
  --bg:#e6e6e6;
  --paper:#ffffff;
  --ink:#2b2b2b;
  --text:#4a4a4a;
  --muted:#8a8a8a;
  --band:#4d4d4d;
  --band-dark:#333333;
  --soft:#d9d9d9;
}
*{margin:0;padding:0;box-sizing:border-box}
html,body{width:1200px;height:1038px;overflow:hidden}
body{background:var(--bg);font-family:'Montserrat',sans-serif;color:var(--text);position:relative}
.letterhead{position:absolute;left:250px;top:24px;width:700px;height:990px;background:var(--paper);box-shadow:0 4px 18px rgba(0,0,0,.12);overflow:hidden}
.brand-mark{position:absolute;left:0;top:110px;width:92px;height:82px;background:var(--band);border-radius:0 10px 10px 0;display:flex;align-items:center;justify-content:center;color:#fff;font-weight:600;font-size:20px;letter-spacing:1px}
.recipient{position:absolute;left:122px;top:112px;font-size:10px;line-height:1.45;color:var(--muted)}
.recipient .to{font-size:9px;color:var(--text)}
.recipient .name{font-size:15px;font-weight:700;color:var(--ink);line-height:1.2}
.recipient .role{color:var(--text)}
.recipient .address{font-weight:700;color:var(--ink)}
.date{position:absolute;right:60px;top:80px;font-size:10px;color:var(--muted)}
.date b{color:var(--ink);font-weight:700}
.body{position:absolute;left:122px;right:60px;top:262px;font-size:11px;line-height:1.65;color:var(--text)}
.body p{margin-bottom:22px}
.signature{position:absolute;left:210px;top:640px}
.signature .sig-mark{width:150px;height:34px;background:var(--soft);border-radius:4px;margin-bottom:6px}
.signature .signer{font-size:16px;font-weight:700;color:var(--ink);letter-spacing:.5px}
.signature .title{font-size:11px;color:var(--muted)}
.contacts{position:absolute;left:180px;top:830px;list-style:none;font-size:11px;font-weight:500;color:var(--ink)}
.contacts li{display:flex;align-items:center;gap:10px;height:34px;white-space:nowrap}
.icon{width:24px;height:24px;flex:0 0 24px;background:var(--band);border-radius:4px;display:flex;align-items:center;justify-content:center}
.footer-band{position:absolute;left:170px;right:0;bottom:22px;height:36px;background:var(--band);display:flex;align-items:center;padding-left:10px;gap:12px;color:#fff;font-size:10px;white-space:nowrap}
.footer-band .icon{background:#fff}
.footer-tab{position:absolute;right:0;bottom:22px;height:36px;width:140px;background:var(--band-dark);clip-path:polygon(16px 0,100% 0,100% 100%,0 100%);color:#fff;font-size:11px;font-weight:600;letter-spacing:.4px;display:flex;align-items:center;justify-content:center;padding-left:10px;white-space:nowrap}
.corner-accent{position:absolute;right:0;bottom:58px;width:30px;height:60px;background:var(--band-dark);clip-path:polygon(100% 0,100% 100%,0 100%)}
</style>
</head>
<body>
<main class="letterhead">
  <div class="brand-mark">TMV</div>

  <div class="recipient">
    <div class="to">To</div>
    <div class="name">Liam Carter</div>
    <div class="role">CEO, ARCVELLSTUDIO</div>
    <div>P: +91 90000 11223, +91 80000 44556</div>
    <div>W: info@arcvellstudio.com, www.arcvellstudio.com</div>
    <div class="address">A: 45 Lake View Road, Pune, India 411001</div>
  </div>

  <div class="date"><b>Date:</b> 24-03-2018</div>

  <section class="body">
    <p>Lorem ipsum dolor sit amet, consectetur adipiscing elit. Pellentesque dictum, ante non ullamcorper convallis, nunc quam blandit metus, ac mollis eros felis a orci. Donec congue, mauris ut pulvinar lobortis, dolor massa feugiat nisl, at tincidunt metus leo vel elit. Proin facilisis semper lobortis. Vivamus augue purus, cursus quis urna non, accumsan pellentesque est. Nulla in iaculis magna, quis aliqu et ex. Cras efficitur metus eget purus euismod facilisis. Proin non metus tincidunt, auctor ipsum a, tempor mi.</p>
    <p>Nulla egestas vulputate risus, ut vestibulum diam commodo id. Mauris ornare libero eu erat porttitor ultrices. Proin sed lectus scelerisque ligula bibendum sagittis ac nec leo. Donec ac accumsan diam, et lobortis mauris.</p>
    <p>Nulla congue volutpat nisl ac lobortis. Integer dignissim interdum libero, quis feugiat velit pretium at. Phasellus sit amet libero rutrum, feugiat odio et, tempus purus.</p>
    <p>Nulla congue volutpat nisl ac lobortis. Integer dignissim interdum libero, quis feugiat velit pretium at. Phasellus sit amet libero rutrum, feugiat odio et, tempus purus. Cras ultricies.</p>
  </section>

  <div class="signature">
    <div class="sig-mark" role="img" aria-label="Handwritten signature"></div>
    <div class="signer">NILS HARDT</div>
    <div class="title">Chairman</div>
  </div>

  <ul class="contacts">
    <li><span class="icon"><svg width="12" height="12" viewBox="0 0 24 24"><path fill="#fff" d="M6.6 10.8a15 15 0 0 0 6.6 6.6l2.2-2.2c.3-.3.7-.4 1-.2 1.1.4 2.3.6 3.6.6.6 0 1 .4 1 1V20c0 .6-.4 1-1 1A17 17 0 0 1 3 4c0-.6.4-1 1-1h3.5c.6 0 1 .4 1 1 0 1.3.2 2.5.6 3.6.1.3 0 .7-.2 1z"/></svg></span>+44 (0) 207 555 0142</li>
    <li><span class="icon"><svg width="12" height="12" viewBox="0 0 24 24"><path fill="none" stroke="#fff" stroke-width="2.4" d="M3 5h18v14H3z M3 5l9 8 9-8"/></svg></span>info@tmv-norlix.com</li>
    <li><span class="icon"><svg width="12" height="12" viewBox="0 0 24 24"><path fill="#fff" d="M6.6 10.8a15 15 0 0 0 6.6 6.6l2.2-2.2c.3-.3.7-.4 1-.2 1.1.4 2.3.6 3.6.6.6 0 1 .4 1 1V20c0 .6-.4 1-1 1A17 17 0 0 1 3 4c0-.6.4-1 1-1h3.5c.6 0 1 .4 1 1 0 1.3.2 2.5.6 3.6.1.3 0 .7-.2 1z"/></svg></span>www.tmv-norlix.com</li>
  </ul>

  <div class="corner-accent"></div>
  <div class="footer-band">
    <span class="icon"><svg width="12" height="12" viewBox="0 0 24 24"><path fill="#4d4d4d" d="M12 2a7 7 0 0 0-7 7c0 5 7 13 7 13s7-8 7-13a7 7 0 0 0-7-7zm0 9.5A2.5 2.5 0 1 1 12 6.5a2.5 2.5 0 0 1 0 5z"/></svg></span>
    <span>4th Floor, 18 Harlow Lane, London EC2A 4LX, United Kingdom</span>
  </div>
  <div class="footer-tab">TMV NORLIX PLC</div>
</main>
</body>
</html>
```